Poster to advertise velquin and dermal fillers

I want a poster to put up in beauty salons to advertise velquin and dermal fillers.
Velquin is used to reduce fine lines and wrinkles around the eyes and across the forehead, between the eyebrows and dermal fillers are used to add volume under the skin where it begins to sag.
The products are mainly used by women.
I am an advanced aesthetic nurse and a member of the Harwell Guild of cosmetic nurses.
I want the poster to be quite feminine with soft colours, eye catching and not too busy, not too much information. It may go in the window of the salon to attract passing trade.
I want it to state that these treatments are available at the particular salon by an advanced trained nurse. "Please ask for further details or to arrange a consultation". etc
My company is called plum Willow

Target Market(s)

Mainly women

Industry/Entity Type

Nurse

Requirements
Should not have
• harsh colours, no jokes

```html
<!DOCTYPE html>
<html lang="en">
<head>
<meta charset="utf-8">
<title>Plum Willow – Velquin and Dermal Fillers</title>
<link rel="stylesheet" href="https://fonts.googleapis.com/css2?family=Alex+Brush&family=Exo+2:wght@400;500&display=swap">
<style>
  :root {
    --sky-top: #b9d9f0;
    --sky-bottom: #ffffff;
    --strip-top: #b36fb0;
    --script-pink: #d27ccd;
    --logo-plum: #a8479f;
    --band-lilac: #c68fc1;
    --footer-magenta: #9b2689;
    --white: #ffffff;
    --petal: #fbfaf6;
    --skin-light: #f4e4dc;
    --skin-warm: #eecbbd;
  }
  * { box-sizing: border-box; margin: 0; padding: 0; }
  html, body {
    width: 1200px;
    height: 800px;
    overflow: hidden;
  }
  body {
    background: linear-gradient(to bottom, var(--sky-top) 0%, var(--sky-bottom) 75%);
    font-family: "Exo 2", sans-serif;
  }
  .poster {
    position: absolute;
    left: 321px;
    top: 7px;
    width: 557px;
    height: 788px;
    overflow: hidden;
    background: var(--petal);
  }
  .poster__strip {
    position: absolute;
    left: 0; top: 0;
    width: 100%;
    height: 8px;
    background: var(--strip-top);
    z-index: 2;
  }
  .poster__photo {
    position: absolute;
    left: 0; top: 8px;
    width: 100%;
    height: 657px;
    background:
      radial-gradient(ellipse at 78% 45%, var(--skin-warm) 0%, rgba(238,203,189,0) 55%),
      linear-gradient(100deg, var(--petal) 0%, #f5f1ec 38%, var(--skin-light) 62%, var(--skin-warm) 100%);
  }
  .brand {
    position: absolute;
    left: 22px;
    top: 40px;
    font-family: "Alex Brush", cursive;
    font-size: 44px;
    line-height: 1;
    color: var(--logo-plum);
  }
  .headline {
    position: absolute;
    font-family: "Alex Brush", cursive;
    color: var(--script-pink);
    line-height: 1;
    white-space: nowrap;
    text-shadow: 1px 1px 0 var(--white), 2px 2px 3px rgba(120, 60, 110, 0.35);
  }
  .headline--do-you   { left: 22px;  top: 212px; font-size: 54px; }
  .headline--want-a   { left: 78px;  top: 285px; font-size: 54px; }
  .headline--more     { left: 46px;  top: 393px; font-size: 104px; }
  .headline--youthful { left: 32px;  top: 522px; font-size: 104px; }
  .headline--appearance { left: 292px; top: 604px; font-size: 54px; }

  .offer {
    position: absolute;
    left: 0; top: 665px;
    width: 100%;
    height: 99px;
    background: var(--band-lilac);
    color: var(--white);
    text-align: center;
    padding-top: 9px;
  }
  .offer__lead {
    font-size: 22px;
    line-height: 29px;
    letter-spacing: 0.3px;
  }
  .offer__note {
    margin-top: 4px;
    font-size: 14px;
    letter-spacing: 0.4px;
    text-transform: uppercase;
  }
  .footer {
    position: absolute;
    left: 0; top: 764px;
    width: 100%;
    height: 24px;
    background: var(--footer-magenta);
    color: var(--white);
    display: flex;
    align-items: center;
    padding-left: 18px;
  }
  .footer__mark {
    font-size: 14px;
    font-weight: 500;
    margin-right: 28px;
  }
  .footer__name {
    font-size: 12px;
    letter-spacing: 4.6px;
    text-transform: uppercase;
  }
</style>
</head>
<body>
  <div class="poster">
    <div class="poster__strip"></div>
    <div class="poster__photo" role="img" aria-label="Close-up beauty portrait of a woman framed by white orchid petals"></div>

    <div class="brand">Plum Willow</div>

    <h1>
      <span class="headline headline--do-you">Do you</span>
      <span class="headline headline--want-a">want a</span>
      <span class="headline headline--more">More</span>
      <span class="headline headline--youthful">Youthful</span>
      <span class="headline headline--appearance">appearance?</span>
    </h1>

    <div class="offer">
      <p class="offer__lead">Velquin and dermal fillers are available<br>at this salon by a qualified aesthetics nurse.</p>
      <p class="offer__note">Please ask for further details or to arrange a consultation.</p>
    </div>

    <div class="footer">
      <span class="footer__mark">hgcn</span>
      <span class="footer__name">Harwell Guild of Cosmetic Nurses</span>
    </div>
  </div>
</body>
</html>
```